Modern Design Business Card industrial maintenance company

Business card design for Company named Brookvale Equipment Services

Target Market(s)

Industrial

Industry/Entity Type

Maintenance and repair

Contact Information for Business Card

Place holder for address, office phone, mobile number and email

Requirements
Must have
• Clean modern look
Nice to have
• N/a

```html
<!DOCTYPE html>
<html lang="en">
<head>
<meta charset="utf-8">
<title>Brookvale Equipment Services – Business Card</title>
<link href="https://fonts.googleapis.com/css2?family=Open+Sans:ital,wght@0,400;0,600;0,700;1,700&display=swap" rel="stylesheet">
<style>
  :root {
    --backdrop: #d3d3d3;
    --paper: #f1f0ee;
    --paper-shade: #e4e3e0;
    --ink: #111111;
    --ink-soft: #7a7a7a;
    --rule: #c9c8c5;
  }
  * { margin: 0; padding: 0; box-sizing: border-box; }
  html, body {
    width: 1200px;
    height: 1051px;
    overflow: hidden;
    background: var(--backdrop);
    font-family: "Open Sans", Arial, sans-serif;
  }
  .sheet {
    position: relative;
    width: 1200px;
    height: 1051px;
  }
  .card {
    position: absolute;
    top: 382px;
    width: 510px;
    height: 292px;
    background: var(--paper);
    box-shadow: 0 6px 18px rgba(0,0,0,0.12);
    overflow: hidden;
  }
  .card--front { left: 60px; }
  .card--back { left: 630px; }

  /* Front */
  .brand {
    position: absolute;
    top: 46px;
    left: 92px;
    display: flex;
    align-items: center;
    gap: 14px;
  }
  .brand__dot {
    width: 46px;
    height: 46px;
    border: 3px solid var(--ink);
    border-radius: 50%;
    flex: none;
  }
  .brand__name {
    font-weight: 700;
    font-size: 19px;
    letter-spacing: 0.06em;
    text-transform: uppercase;
    color: var(--ink);
    line-height: 1.15;
  }
  .person {
    position: absolute;
    top: 138px;
    left: 40px;
    width: 200px;
    text-align: right;
  }
  .person__name {
    font-weight: 700;
    font-size: 17px;
    color: var(--ink);
    text-transform: uppercase;
    line-height: 1.2;
  }
  .person__role {
    font-weight: 700;
    font-style: italic;
    font-size: 11px;
    color: var(--ink-soft);
    margin-bottom: 8px;
  }
  .person__address {
    font-size: 12px;
    color: var(--ink-soft);
    line-height: 1.5;
  }
  .divider {
    position: absolute;
    top: 150px;
    left: 262px;
    width: 1px;
    height: 100px;
    background: var(--rule);
  }
  .contacts {
    position: absolute;
    top: 154px;
    left: 280px;
    list-style: none;
  }
  .contacts li {
    display: flex;
    align-items: center;
    gap: 8px;
    font-size: 12.5px;
    color: var(--ink-soft);
    line-height: 22px;
  }
  .contacts svg { width: 11px; height: 11px; flex: none; }

  /* Back */
  .back-texture {
    position: absolute;
    inset: 0;
    background: radial-gradient(circle at 50% 50%, var(--paper) 0%, var(--paper-shade) 100%);
  }
  .back-mark {
    position: absolute;
    top: 50%;
    left: 50%;
    transform: translate(-50%, -50%);
    font-weight: 700;
    font-size: 14px;
    letter-spacing: 0.06em;
    text-transform: uppercase;
    color: var(--ink);
    text-align: center;
    line-height: 1.25;
    white-space: nowrap;
  }
</style>
</head>
<body>
<main class="sheet">
  <section class="card card--front" aria-label="Business card front">
    <div class="brand">
      <span class="brand__dot"></span>
      <span class="brand__name">Brookvale<br>Equipment Services</span>
    </div>

    <div class="person">
      <p class="person__name">Dorian Keller</p>
      <p class="person__role">President</p>
      <p class="person__address">1840 Harbor Ridge Rd<br>Lakemont CA 90417</p>
    </div>

    <span class="divider"></span>

    <ul class="contacts">
      <li>
        <svg viewBox="0 0 12 12" aria-hidden="true"><rect x="3" y="0.5" width="6" height="11" rx="1" fill="none" stroke="#111" stroke-width="1.2"/><circle cx="6" cy="9.5" r="0.7" fill="#111"/></svg>
        555-310-4872
      </li>
      <li>
        <svg viewBox="0 0 12 12" aria-hidden="true"><path d="M2.5 1 L4.5 1 L5.5 3.5 L4.2 4.6 Q5.2 6.8 7.4 7.8 L8.5 6.5 L11 7.5 L11 9.5 Q10.5 11 9 11 Q1 10 1 2.5 Q1 1 2.5 1 Z" fill="#111"/></svg>
        555-310-4872
      </li>
      <li>
        <svg viewBox="0 0 12 12" aria-hidden="true"><rect x="0.5" y="2.5" width="11" height="7.5" fill="#111"/><path d="M0.5 2.5 L6 7 L11.5 2.5" fill="none" stroke="#f1f0ee" stroke-width="1"/></svg>
        dkeller@brookvale.com
      </li>
      <li>
        <svg viewBox="0 0 12 12" aria-hidden="true"><circle cx="6" cy="6" r="5.3" fill="none" stroke="#111" stroke-width="1.2"/><ellipse cx="6" cy="6" rx="2.2" ry="5.3" fill="none" stroke="#111" stroke-width="1"/><line x1="0.7" y1="6" x2="11.3" y2="6" stroke="#111" stroke-width="1"/></svg>
        www.brookvale.com
      </li>
    </ul>
  </section>

  <section class="card card--back" aria-label="Business card back">
    <div class="back-texture" role="img" aria-label="Embossed decorative pattern on white card stock"></div>
    <p class="back-mark">Brookvale<br>Equipment Services</p>
  </section>
</main>
</body>
</html>
```